Tallbrook Meridian Advisory needs business cards

Tallbrook Meridian Advisory is a new approach to consulting: we believe in partnering our clients in a hands-on, side-by-side, rolling-up-our sleeves approach, rather than being removed and aloof consultants.

We have a logo design developped through PixelHarbor (see attachment) and need to move to the stage of designing a business card for our 7 founding members.

Target Market(s)

Senior executives in local and global companies (such as Fizzmont Tonic, Hollanby, Brevard, etc)

Industry/Entity Type

Business

Requirements
Must have
• Look and feel: The design reflect the logo: i.e. professional, modern and approachable (as opposed to corporate traditional and remote). We are looking for a high quality, premium design.

Content must haves:
- prominent: our logo, person's name, function, phone number and e-mail address
- less prominent: company address and website

Example: Tallbrook Meridian Advisory logo, Mireille Vostag, Partner, +44 (0)781 209 3375, mireille_vostag@tallbrookmeridian.example / 17 Pelham Crescent, Esher, Surrey, UK, KT10 3WN - www.tallbrookmeridian.example

- Both sides of the card can be used
- Both versions of the logo can be used (on black or on white)

```html
<!DOCTYPE html>
<html lang="en">
<head>
<meta charset="utf-8">
<title>Tallbrook Meridian Advisory — Business Card</title>
<link rel="stylesheet" href="https://fonts.googleapis.com/css2?family=Exo+2:wght@400;600;700&display=swap">
<style>
  :root {
    --page-bg: #eceff2;
    --ink: #1e2327;
    --ink-soft: #5a6066;
    --brand-blue: #1b8fd8;
    --brand-blue-deep: #0f6fb3;
    --tint-1: #cfe9f8;
    --tint-2: #eef8fe;
    --tint-3: #b9def4;
    --square: rgba(120, 196, 238, 0.35);
    --square-soft: rgba(150, 210, 242, 0.22);
    --card-white: #ffffff;
  }
  * { box-sizing: border-box; margin: 0; padding: 0; }
  html, body { width: 1200px; height: 900px; overflow: hidden; }
  body {
    background: var(--page-bg);
    font-family: "Exo 2", sans-serif;
    color: var(--ink);
    position: relative;
  }
  .card {
    position: absolute;
    left: 280px;
    width: 640px;
    height: 366px;
    border-radius: 4px;
    overflow: hidden;
    box-shadow: 0 6px 22px rgba(0, 0, 0, 0.12);
  }
  .card--front {
    top: 52px;
    background: linear-gradient(115deg, var(--tint-1) 0%, var(--tint-2) 48%, var(--tint-3) 100%);
  }
  .card--back {
    top: 482px;
    background: var(--card-white);
  }
  .deco {
    position: absolute;
    border-radius: 14px;
    background: var(--square);
  }
  .deco--soft { background: var(--square-soft); }

  /* front */
  .brand {
    position: absolute;
    left: 120px;
    top: 118px;
    display: flex;
    align-items: center;
    gap: 18px;
  }
  .brand__dot {
    width: 74px;
    height: 74px;
    border-radius: 50%;
    background: var(--brand-blue);
    flex: none;
  }
  .brand__name {
    font-size: 30px;
    font-weight: 600;
    color: var(--ink);
    line-height: 1.1;
    letter-spacing: 0.01em;
  }
  .front__web {
    position: absolute;
    left: 196px;
    top: 236px;
    font-size: 16px;
    color: var(--ink);
    letter-spacing: 0.02em;
  }

  /* back */
  .back__disc {
    position: absolute;
    right: 70px;
    top: -30px;
    width: 150px;
    height: 150px;
    border-radius: 50%;
    background: var(--brand-blue);
  }
  .person {
    position: absolute;
    left: 24px;
    top: 120px;
    display: flex;
    align-items: baseline;
    gap: 8px;
  }
  .person__name { font-size: 24px; font-weight: 700; color: var(--ink); }
  .person__role {
    font-size: 17px;
    font-weight: 400;
    color: var(--ink-soft);
    border-left: 2px solid var(--ink);
    padding-left: 6px;
    letter-spacing: 0.04em;
  }
  .contact {
    position: absolute;
    left: 24px;
    top: 270px;
    list-style: none;
    display: flex;
    flex-direction: column;
    gap: 8px;
  }
  .contact__item { display: flex; align-items: center; gap: 12px; font-size: 17px; color: var(--ink); }
  .contact__icon {
    width: 20px; height: 20px;
    border-radius: 3px;
    background: var(--brand-blue);
    color: #fff;
    font-size: 14px;
    font-weight: 600;
    display: flex; align-items: center; justify-content: center;
  }
  .address {
    position: absolute;
    left: 420px;
    top: 222px;
    font-size: 13px;
    line-height: 1.45;
    color: var(--ink);
    font-style: normal;
  }
</style>
</head>
<body>
  <section class="card card--front" aria-label="Card front">
    <div class="deco" style="left:40px;top:100px;width:90px;height:100px;"></div>
    <div class="deco deco--soft" style="left:90px;top:140px;width:110px;height:120px;"></div>
    <div class="deco" style="left:520px;top:40px;width:60px;height:56px;"></div>
    <div class="deco deco--soft" style="left:548px;top:16px;width:80px;height:90px;"></div>
    <div class="brand">
      <span class="brand__dot"></span>
      <span class="brand__name">Tallbrook Meridian<br>Advisory</span>
    </div>
    <p class="front__web">www.tallbrookmeridian.example</p>
  </section>

  <section class="card card--back" aria-label="Card back">
    <div class="back__disc"></div>
    <div class="deco" style="left:30px;top:20px;width:120px;height:110px;"></div>
    <div class="deco deco--soft" style="left:120px;top:80px;width:80px;height:75px;"></div>
    <div class="deco" style="left:110px;top:150px;width:50px;height:50px;"></div>
    <div class="deco" style="left:380px;top:150px;width:120px;height:100px;"></div>
    <div class="deco deco--soft" style="left:290px;top:210px;width:380px;height:180px;border-radius:24px;"></div>
    <div class="person">
      <span class="person__name">Mireille Vostag</span>
      <span class="person__role">PARTNER</span>
    </div>
    <ul class="contact">
      <li class="contact__item"><span class="contact__icon">t</span>+44 (0)781 209 3375</li>
      <li class="contact__item"><span class="contact__icon">e</span>mireille_vostag@tallbrookmeridian.example</li>
    </ul>
    <address class="address">17 Pelham Crescent, Esher<br>Surrey, UK, KT10 3WN</address>
  </section>
</body>
</html>
```